business card deign

Logo needs the following on it.
1. attached logo
2. Tagline - "If it keeps a drink cold or the party going...we do it!"
3. Name- Delia Fenwick, Founder and CPO
4. Address - 418 E. Harlow Avenue, Ste 2204, Tampa, FL. 33719
5. Phone - 720.555.0187

```html
<!DOCTYPE html>
<html lang="en">
<head>
<meta charset="utf-8">
<title>Hopley Business Card</title>
<link rel="stylesheet" href="https://fonts.googleapis.com/css2?family=Archivo:wght@400;700&display=swap">
<style>
  :root {
    --backdrop: #3b3b3b;
    --card-black: #050505;
    --panel-white: #ffffff;
    --silver: #c9c9c9;
    --silver-dark: #9a9a9a;
    --ink-light: #f2f2f2;
    --muted: #d6d6d6;
  }
  * { box-sizing: border-box; margin: 0; padding: 0; }
  html, body {
    width: 1200px;
    height: 689px;
    overflow: hidden;
    background: var(--backdrop);
    font-family: "Archivo", Arial, sans-serif;
  }
  .stage {
    position: relative;
    width: 1200px;
    height: 689px;
  }
  .card {
    position: absolute;
    top: 196px;
    width: 525px;
    height: 300px;
    border-radius: 18px;
    background: var(--card-black);
    overflow: hidden;
  }
  .card--front { left: 50px; }
  .card--back { left: 625px; }

  .front-brand {
    position: absolute;
    left: 0;
    right: 0;
    top: 126px;
    text-align: center;
    font-weight: 700;
    font-size: 44px;
    letter-spacing: 22px;
    padding-left: 22px;
    color: var(--silver);
  }

  .back-illustration {
    position: absolute;
    left: 0;
    top: 0;
    width: 215px;
    height: 100%;
    background: var(--panel-white);
  }
  .back-illustration .figure {
    position: absolute;
    left: 70px;
    top: 30px;
    width: 190px;
    height: 270px;
    border-radius: 60px 60px 0 0;
    background: linear-gradient(160deg, #1a1a1a, #000000);
  }

  .back-info {
    position: absolute;
    right: 30px;
    top: 24px;
    width: 270px;
    text-align: right;
    color: var(--ink-light);
  }
  .back-brand {
    font-weight: 700;
    font-size: 24px;
    letter-spacing: 11px;
    margin-right: -11px;
    margin-bottom: 24px;
  }
  .holder-name {
    font-weight: 700;
    font-size: 16px;
    text-transform: uppercase;
  }
  .holder-title {
    font-size: 12px;
    color: var(--muted);
    margin-bottom: 12px;
  }
  .address-line {
    font-size: 12.5px;
    line-height: 17px;
    color: var(--muted);
  }
  .contact-list {
    list-style: none;
    margin-top: 14px;
  }
  .contact-item {
    display: flex;
    justify-content: flex-end;
    align-items: center;
    gap: 8px;
    font-size: 12.5px;
    line-height: 18px;
    color: var(--muted);
  }
  .contact-icon {
    width: 11px;
    height: 11px;
    fill: var(--ink-light);
  }
</style>
</head>
<body>
<main class="stage">
  <section class="card card--front" aria-label="Card front">
    <div class="front-brand">HOPLEY</div>
  </section>

  <section class="card card--back" aria-label="Card back">
    <div class="back-illustration">
      <div class="figure" role="img" aria-label="Large black kangaroo silhouette illustration"></div>
    </div>
    <div class="back-info">
      <div class="back-brand">HOPLEY</div>
      <div class="holder-name">Delia Fenwick</div>
      <div class="holder-title">Founder and CPO</div>
      <div class="address-line">418 E. Harlow Avenue</div>
      <div class="address-line">Ste 2204</div>
      <div class="address-line">Tampa, FL. 33719</div>
      <ul class="contact-list">
        <li class="contact-item">720.555.0187
          <svg class="contact-icon" viewBox="0 0 12 12" aria-hidden="true"><path d="M2.5 0.5l2 2.2-1 1.3c.7 1.6 2 2.9 3.5 3.6l1.3-1 2.2 2-1.3 2.4C5 10.8 1.2 7 0.1 1.8z"/></svg>
        </li>
        <li class="contact-item">info@hopley.com
          <svg class="contact-icon" viewBox="0 0 12 12" aria-hidden="true"><path d="M0 2.5h12v7H0z M0.6 3L6 7 11.4 3" stroke="#050505" stroke-width="0.8"/></svg>
        </li>
        <li class="contact-item">www.hopley.com
          <svg class="contact-icon" viewBox="0 0 12 12" aria-hidden="true"><circle cx="6" cy="6" r="5.5"/><path d="M0.5 6h11M6 0.5c-2.4 3-2.4 8 0 11M6 0.5c2.4 3 2.4 8 0 11" stroke="#050505" stroke-width="0.8" fill="none"/></svg>
        </li>
      </ul>
    </div>
  </section>
</main>
</body>
</html>
```